Diverse business needs a corporate identity system

Varrow Brisk Holdings Limited is a well established family owned and run business operating in Port Moresby, Papua New Guinea since 1989. As part of taking the business to the next level, we are redoing our branding/corporate identity.

We currently carry out two core business activities servicing corporate clients in the commercial and industrial sectors:
1. Electrical - new installations and maintenance work
2. Construction - mostly commercial & industrial, some residential

We are looking to add the following business activities in near future:
1. IT consulting
2. Property development - business/industrial park, residential complexes, low cost housing
3. Retail of hardware, construction supplies and flat pack furniture & kitchens

We have just completed our logo design here on SketchHarbor and now wanting to design business card and stationery based on our new logo (attached).

Deliverables are:
1. Business card - double sided
2. Letterhead A4

Details to go on the card:
Name: Martin Fenwale
Title: Director
Email: martin.fenwale@varrowbrisk.example
Tel: +675 3481720, +675 3487043
Office: Section 17 Lot 43, Kessaby Light Industrial Area, Port Moresby, Papua New Guinea
Postal: PO Box 914, Kessaby, NCD, Papua New Guinea
Website: varrowbrisk.example

Our services can be listed somewhere on the card:
Electrical, Construction, Property Development, IT Consulting

Details to go on the letterhead:
Varrow Brisk Holdings Ltd.
PO Box 914, Kessaby, NCD, Papua New Guinea
Fax: +675 3486158
Email: info@varrowbrisk.example

For inspiration, I have uploaded some images of business cards we like.

Would be good if the same/similar business card design could be printed both economically (e.g. full coloured both sides, matte card stock) for majority of staff and upscaled to use premium features such as letter pressed, foil etc for use by executives. Otherwise, please provide two separate designs.

Logo text font is nexa bold freefont - please use something from nexa family or another font type that complements it.

Reason: Few designs were submitted. Most were clearly from ready to use templates. No designs really stand out for us at the moment. So we have decided to narrow the focus to just business card and A4 letterhead. And also revised the brief to be completely open to hopefully invite more creative designs.

I have updated the brief to be a lot less restrictive to try and get more creative designs. Also uploaded more images of premium business cards for inspiration.

Construction

Requirements
Must have
• All designs must conform to quillpress specifications. Refer to and download appropriate work file templates from http://www.quillpress.example/uploads/templates.aspx?ref=5820146631&tab=0.
Should not have
• No QR codes and social media links.

```html
<!DOCTYPE html>
<html lang="en">
<head>
<meta charset="utf-8">
<title>Varrow Brisk Holdings – Business Cards</title>
<link href="https://fonts.googleapis.com/css2?family=Nunito:wght@400;700;800&display=swap" rel="stylesheet">
<style>
  :root {
    --backdrop: #2a2a2a;
    --brand-red: #cf3a2c;
    --brand-yellow: #e5b719;
    --card-white: #f4f4f2;
    --ink-grey: #6d6d6d;
    --ink-dark: #555;
    --ink-light: #ffffff;
  }
  * { margin: 0; padding: 0; box-sizing: border-box; }
  html, body {
    width: 1200px; height: 900px; overflow: hidden;
    background: var(--backdrop);
    font-family: "Nunito", sans-serif;
  }
  .stage { position: relative; width: 1200px; height: 900px; }
  .card { position: absolute; width: 488px; height: 278px; overflow: hidden; }

  /* Front: personal details */
  .card-front { left: 75px; top: 307px; background: var(--card-white); }
  .holder { position: absolute; left: 28px; top: 60px; }
  .holder-name { color: var(--brand-red); font-weight: 800; font-size: 17px; }
  .holder-title { color: var(--ink-grey); font-size: 12.5px; letter-spacing: .4px; margin-top: 1px; }
  .front-mark { position: absolute; right: 30px; top: 36px; display: flex; align-items: center; gap: 6px; }
  .front-mark .dot { width: 26px; height: 26px; border-radius: 50%; background: var(--brand-red); }
  .front-mark .word { color: var(--brand-red); font-weight: 800; font-size: 15px; }
  .contact-list { position: absolute; left: 28px; top: 182px; list-style: none; font-size: 13px; color: var(--ink-grey); line-height: 17px; }
  .contact-list li { display: flex; align-items: center; gap: 4px; }
  .contact-list svg { width: 11px; height: 11px; fill: var(--brand-red); }
  .company-block { position: absolute; left: 283px; right: 16px; top: 182px; font-size: 13px; font-style: normal; color: var(--ink-grey); line-height: 17px; white-space: nowrap; }
  .company-name { color: var(--brand-red); font-weight: 800; font-size: 12.5px; }
  .company-web { color: var(--ink-dark); font-weight: 800; font-size: 11px; letter-spacing: 1.1px; }

  /* Back: brand sides */
  .card-back { left: 632px; display: flex; flex-direction: column; align-items: center; }
  .card-back.yellow { top: 160px; background: var(--brand-yellow); }
  .card-back.red { top: 455px; background: var(--brand-red); }
  .brand-lockup { display: flex; align-items: center; gap: 14px; margin-top: 100px; height: 72px; }
  .brand-lockup .dot { width: 62px; height: 62px; border-radius: 50%; }
  .brand-lockup .word { font-weight: 800; font-size: 50px; letter-spacing: -.5px; }
  .yellow .dot { background: var(--brand-red); }
  .yellow .word { color: var(--brand-red); }
  .red .dot { background: var(--brand-yellow); }
  .red .word { color: var(--brand-yellow); }
  .services { margin-top: 64px; color: var(--ink-light); font-weight: 700; font-size: 13.5px; }
</style>
</head>
<body>
<main class="stage">

  <section class="card card-front">
    <div class="holder">
      <div class="holder-name">Dorian Kellam</div>
      <div class="holder-title">PRESIDENT</div>
    </div>
    <div class="front-mark"><span class="dot"></span><span class="word">Varrow Brisk</span></div>

    <ul class="contact-list">
      <li><svg viewBox="0 0 12 12"><path d="M2.5 1l2 2.2-1 1.3a7 7 0 0 0 4 4l1.3-1 2.2 2-1.3 1.5C5 11 1 7 1 2.3z"/></svg>• 675-348-1720</li>
      <li><svg viewBox="0 0 12 12"><path d="M3 0h6v12H3zM4 1.5v7.5h4V1.5z"/></svg>• 675-348-7043</li>
      <li><svg viewBox="0 0 12 12"><path d="M3 1h6v3H3zM1 4.5h10V10H9V8H3v2H1zM3.5 8.5h5V12h-5z"/></svg>• 675-348-6158</li>
      <li><svg viewBox="0 0 12 12"><path d="M0 2h12v1.2L6 7 0 3.2zM0 4.6l6 3.8 6-3.8V10H0z"/></svg>• dorian@varrowbrisk.example</li>
    </ul>

    <address class="company-block">
      <div class="company-name">Varrow Brisk Holdings Ltd.</div>
      <div>Section 17 Lot 43 Kessaby</div>
      <div>Port Moresby, NCD</div>
      <div>Papua New Guinea</div>
      <div class="company-web">www.varrowbrisk.example</div>
    </address>
  </section>

  <section class="card card-back yellow">
    <div class="brand-lockup"><span class="dot"></span><span class="word">Varrow Brisk</span></div>
    <p class="services">Electrical • Construction • Property Development • IT Consulting</p>
  </section>

  <section class="card card-back red">
    <div class="brand-lockup"><span class="dot"></span><span class="word">Varrow Brisk</span></div>
    <p class="services">Electrical • Construction • Property Development • IT Consulting</p>
  </section>

</main>
</body>
</html>
```